Business Card design for leader Solar Energy company
Loreno Energy Group
Professional
Belisa Torv
CEO
Santo Domingo: Calle Olmeda Vieja #418, Edif. Torv Corporativo, Suite 512
Las Terrenas: Calle de las Brisas, Coral Vista Plaza, Suite 512
Punta Cana; Proximamente
809.741.LORE (5673)
belisa@lorenopower-example.com
www.lorenopower-example.com
Think Green, Save Money, Go Solar.
Please use this logo for the business card design.
Thank you,
-belisa
vector logo

```html
<!DOCTYPE html>
<html lang="en">
<head>
<meta charset="utf-8">
<title>Loreno Energy Group – Business Card</title>
<link href="https://fonts.googleapis.com/css2?family=Questrial&family=Open+Sans:ital,wght@0,400;0,600;0,700;1,700&display=swap" rel="stylesheet">
<style>
  :root {
    --bg: #e9e6e1;
    --card-white: #ffffff;
    --brand-green: #3f8a3a;
    --brand-blue: #1f4f93;
    --band-light: #e8eef6;
    --ink: #3a3a3a;
    --ink-soft: #555555;
    --logo-grey: #6f6f6f;
  }
  * { box-sizing: border-box; margin: 0; padding: 0; }
  html, body { width: 1200px; height: 402px; overflow: hidden; background: var(--bg); }
  body { position: relative; font-family: "Open Sans", Arial, sans-serif; }

  .card {
    position: absolute;
    top: 38px;
    width: 552px;
    height: 322px;
    box-shadow: 0 3px 10px rgba(0,0,0,0.25);
  }
  .card--front { left: 36px; background: var(--card-white); }
  .card--back  { left: 620px; background: var(--brand-green); }

  /* wordmark */
  .wordmark { position: absolute; display: flex; align-items: center; gap: 12px; }
  .wordmark__dot { width: 22px; height: 22px; border-radius: 50%; background: var(--brand-green); }
  .wordmark__name {
    font-family: "Questrial", Arial, sans-serif;
    font-size: 30px;
    letter-spacing: 2px;
    color: var(--logo-grey);
    line-height: 1;
  }
  .card--front .wordmark { left: 28px; top: 50px; }
  .card--back .wordmark { left: 0; right: 0; top: 110px; justify-content: center; }
  .card--back .wordmark__name { color: #ffffff; font-size: 38px; }
  .card--back .wordmark__dot { background: #ffffff; width: 26px; height: 26px; }

  /* name band */
  .name-band { position: absolute; left: 0; right: 0; top: 176px; height: 30px; display: flex; }
  .name-band__label {
    width: 205px; background: var(--band-light);
    color: var(--brand-blue); font-weight: 700; font-size: 14px;
    padding-left: 28px; line-height: 30px;
  }
  .name-band__label span { font-weight: 400; }
  .name-band__blue { flex: 1; background: var(--brand-blue); }
  .name-band__green { width: 58px; background: var(--brand-green); margin: 0 4px; }
  .name-band__end { width: 60px; background: var(--brand-blue); }

  /* contacts */
  .contacts { position: absolute; left: 28px; top: 222px; list-style: none; }
  .contacts li {
    display: flex; align-items: center; gap: 6px;
    font-size: 10.5px; color: var(--ink); line-height: 15px;
  }
  .contacts svg { width: 10px; height: 10px; flex: none; }
  .address {
    position: absolute; left: 28px; top: 288px;
    font-size: 9.5px; line-height: 13px; color: var(--ink-soft);
  }

  .tagline {
    position: absolute; left: 0; right: 0; top: 176px; text-align: center;
    color: #ffffff; font-style: italic; font-weight: 700; font-size: 17px;
  }
</style>
</head>
<body>

<section class="card card--front" aria-label="Card front">
  <div class="wordmark">
    <span class="wordmark__dot"></span>
    <span class="wordmark__name">Loreno Energy Group</span>
  </div>

  <div class="name-band">
    <div class="name-band__label">Belisa Torv, <span>CEO</span></div>
    <div class="name-band__blue"></div>
    <div class="name-band__green"></div>
    <div class="name-band__end"></div>
  </div>

  <ul class="contacts">
    <li><svg viewBox="0 0 10 10"><path d="M2 1h2l1 2-1 1a5 5 0 0 0 2 2l1-1 2 1v2c0 1-1 1-1 1A8 8 0 0 1 1 2s0-1 1-1z" fill="#3f8a3a"/></svg>809.741.LORE (5673)</li>
    <li><svg viewBox="0 0 10 10"><rect x="2.5" y="0.5" width="5" height="9" rx="1" fill="#3f8a3a"/></svg>829-555-0147</li>
    <li><svg viewBox="0 0 10 10"><rect x="0.5" y="2" width="9" height="6" fill="#3f8a3a"/><path d="M1 2.5l4 3 4-3" stroke="#fff" fill="none" stroke-width="0.8"/></svg>belisa@lorenopower-example.com</li>
    <li><svg viewBox="0 0 10 10"><circle cx="5" cy="5" r="4.2" fill="none" stroke="#3f8a3a" stroke-width="1.2"/><path d="M1 5h8M5 1v8" stroke="#3f8a3a" stroke-width="0.8"/></svg>www.lorenopower-example.com</li>
  </ul>

  <p class="address">
    Santo Domingo: Calle Olmeda Vieja #418, Edif. Torv Corporativo, Suite 512<br>
    Las Terrenas: Calle de las Brisas, Coral Vista Plaza, Suite 512, Punta Cana: Proximamente
  </p>
</section>

<section class="card card--back" aria-label="Card back">
  <div class="wordmark">
    <span class="wordmark__dot"></span>
    <span class="wordmark__name">Loreno Energy Group</span>
  </div>
  <p class="tagline">Think Green • Save Money • Go Solar.</p>
</section>

</body>
</html>
```